Powerpoint template design for Oil and Gas Investment Fund Pitchdeck

I need a template design for an oil and gas investment fund pitch deck. Design needs to be clean and have plenty of space for inserting graphics. Audience is high net worth individuals and corporate finance executives (private equity firms). We will need a title page with our logo and some oil& gas images (some included already) and the template for the internal pages. A rough example is attached. I would like to keep the current page dimensions because we have many financial charts we will want to add to the template pages. So the template will need to include title page, internal page, and a team page.

Target Market(s)

High etw worth individual investors and corporate finance professionals

Industry/Entity Type

Oil an dgas investment fund

Font styles to use
Serif

Requirements
Must have
• title page, interior page, team page

```html
<!DOCTYPE html>
<html lang="en">
<head>
<meta charset="utf-8">
<title>Ironvale Energy Partners – Pitch Deck Template</title>
<link rel="stylesheet" href="https://fonts.googleapis.com/css2?family=Tinos:ital,wght@0,400;0,700;1,400;1,700&family=Roboto:wght@300;400;700&display=swap">
<style>
  :root{
    --ink:#0d0d0d;
    --paper:#ffffff;
    --canvas:#ebebeb;
    --grey:#8a8a8a;
    --light:#b9b9b9;
    --row:#e3e3e8;
    --serif:'Tinos', 'Times New Roman', serif;
    --sans:'Roboto', Arial, sans-serif;
  }
  *{margin:0;padding:0;box-sizing:border-box}
  html,body{width:1200px;height:3000px;overflow:hidden;background:var(--canvas)}
  .deck{position:relative;width:1200px;height:3000px}
  .slide{position:absolute;width:551px;height:312px;background:var(--paper);overflow:hidden;font-family:var(--serif);color:var(--ink);box-shadow:0 1px 3px rgba(0,0,0,.12)}
  .abs{position:absolute}
  .photo{position:absolute}
  .hd-bar{position:absolute;left:0;top:24px;width:30px;height:10px;background:var(--ink)}
  .hd-title{position:absolute;left:42px;top:17px;font-size:16px;font-weight:700}
  .foot-bar{position:absolute;left:0;top:286px;width:478px;height:12px;background:var(--ink)}
  .foot-mark{position:absolute;left:484px;top:289px;font-size:4.5px;letter-spacing:.5px;font-weight:700}
  .foot-num{position:absolute;left:528px;top:286px;width:23px;height:12px;background:var(--ink);color:#fff;font-family:var(--sans);font-size:5px;text-align:center;line-height:12px}
  .lead{position:absolute;font-size:15.5px;line-height:21px;color:var(--ink)}
  .stat{position:absolute;font-family:var(--sans)}
  .stat b{display:block;font-weight:300;font-size:18px}
  .stat i{display:block;font-style:normal;font-weight:700;font-size:4.5px;margin-top:6px;letter-spacing:.3px}
  .stat span{display:block;font-weight:300;font-size:4.5px;color:var(--grey);margin-top:2px}
  .stat.on-dark{color:#fff}
  .stat.on-dark span{color:#bbb}
  .tiny{font-family:var(--sans);font-weight:300;font-size:4.5px;line-height:7px;color:var(--grey)}
  .caption{position:absolute;width:115px}
  .caption b{display:block;font-family:var(--sans);font-size:4.5px;font-weight:700;margin-bottom:3px}
  /* team */
  .team-box{position:absolute;left:32px;top:52px;width:285px;height:200px;background:var(--ink)}
  .member{position:absolute;width:90px;text-align:center;font-size:6px;line-height:7px}
  .member .portrait{width:62px;height:62px;margin:0 auto 8px}
  .member h4{font-size:8px;font-weight:700;margin-bottom:2px}
  .member em{display:block;font-weight:700}
  .team-box .member{color:#fff}
  .portrait{background:linear-gradient(160deg,#5a5a5a,#1d1d1d 70%)}
  .adv-title{position:absolute;left:337px;top:55px;width:160px;text-align:center;font-size:8px;font-weight:700}
  /* partners: plain names, one colour, one weight */
  .partner{position:absolute;font-family:var(--serif);font-size:13px;font-weight:400;line-height:15px;color:var(--ink);display:flex;align-items:center;gap:6px;white-space:nowrap}
  .partner .sq{flex:none;width:10px;height:10px;background:var(--ink)}
  /* table */
  .tbl-head{position:absolute;top:61px;font-family:var(--sans);font-size:5px;font-weight:700}
  .tbl-row{position:absolute;left:30px;width:495px;height:20px;font-size:4.5px;line-height:20px}
  .tbl-row.alt{background:var(--row)}
  .tbl-row .no{position:absolute;left:8px}
  .tbl-row .pn{position:absolute;left:40px;width:190px;text-align:center}
  .tbl-row .au{position:absolute;left:255px;width:80px;text-align:center}
  .tbl-row .pr{position:absolute;left:370px;top:9.5px;height:1.5px;background:var(--ink)}
  /* charts */
  .ring{position:absolute;width:90px;text-align:center;font-family:var(--sans)}
  .ring .num{position:absolute;left:0;top:34px;width:90px;font-weight:300;font-size:17px}
  .ring .num small{font-size:5px}
  .ring b{display:block;font-size:4.5px;font-weight:700;margin-top:22px}
  .bar-caption{position:absolute;width:190px;text-align:center;font-family:var(--sans)}
  .bar-caption b{display:block;font-size:4.5px;font-weight:700;margin-bottom:3px}
  /* cover */
  .cover{position:absolute;left:150px;top:265px;width:900px;height:510px;overflow:hidden;box-shadow:0 2px 8px rgba(0,0,0,.2)}
  .cover-name{position:absolute;left:58px;top:300px;display:flex;align-items:center;gap:10px;color:#fff;font-family:var(--serif);font-size:26px;letter-spacing:3px}
  .cover-name .sq{width:16px;height:16px;background:#fff}
  .cover-tag{position:absolute;left:58px;top:380px;color:#fff;font-family:var(--serif);font-weight:700;font-size:15px;line-height:26px}
  .thanks{position:absolute;left:0;top:128px;width:551px;text-align:center;font-family:var(--serif);font-size:52px;color:#111;letter-spacing:1px}
</style>
</head>
<body>
<div class="deck">

  <!-- Cover slide -->
  <section class="cover">
    <div class="photo" style="inset:0;background:linear-gradient(180deg,#6e6a80 0%,#c7928a 30%,#e6b48e 45%,#3b4656 62%,#222a33 100%)" role="img" aria-label="Offshore oil platform at sunset over the sea"></div>
    <svg class="abs" style="left:0;top:0" width="900" height="510" viewBox="0 0 900 510">
      <polygon points="0,0 185,0 500,510 0,510" fill="#0d0d0d"/>
    </svg>
    <div class="cover-name"><span class="sq"></span>IRONVALE ENERGY PARTNERS</div>
    <div class="cover-tag">Consolidating Profitable Conventional<br>West Texas Oil &amp; Gas Wells Into A<br>High Return Investment Fund</div>
  </section>

  <!-- 2: Title page -->
  <section class="slide" style="left:38px;top:1040px">
    <div class="photo" style="left:0;top:0;width:551px;height:156px;background:linear-gradient(180deg,#c6c3b6 0%,#b0ab99 55%,#5e5a4c 80%,#8b8676 100%)" role="img" aria-label="Oil pumpjacks silhouetted in a misty field"></div>
    <div class="abs" style="left:58px;top:175px;font-size:15px;font-weight:700">Title Here?</div>
    <p class="abs" style="left:58px;top:200px;width:445px;font-size:6px;line-height:8px">Lorem ipsum dolor sit amet, consectetuer adipiscing elit. Maecenas porttitor congue massa. Fusce posuere, magna sed pulvinar ultricies, purus lectus malesuada libero, sit amet commodo magna eros quis urna. Nunc viverra imperdiet enim. Fusce est. Vivamus a tellus. Pellentesque habitant morbi tristique senectus et netus et malesuada fames ac turpis egestas. Proin pharetra nonummy pede. Mauris et orci. Lorem ipsum dolor sit amet, consectetuer adipiscing elit. Maecenas porttitor congue massa. Fusce posuere, magna sed pulvinar ultricies, purus lectus malesuada libero, sit amet commodo magna eros quis urna.</p>
    <div class="foot-bar"></div><div class="foot-mark">IRONVALE</div><div class="foot-num">2</div>
  </section>

  <!-- 3: Solutions -->
  <section class="slide" style="left:609px;top:1040px">
    <div class="hd-bar"></div><div class="hd-title">Text here</div>
    <div class="photo" style="left:29px;top:80px;width:115px;height:115px;background:linear-gradient(180deg,#7f9fc4,#a9b4b8 55%,#5d5a52)" role="img" aria-label="Refinery flare stack under blue sky"></div>
    <div class="photo" style="left:156px;top:80px;width:115px;height:115px;background:linear-gradient(180deg,#c79a45,#8d5e22 60%,#3a2a14)" role="img" aria-label="Pumpjack at golden sunset"></div>
    <div class="photo" style="left:283px;top:80px;width:115px;height:115px;background:linear-gradient(180deg,#8fb0d4,#8d8f94 50%,#5e6470)" role="img" aria-label="Refinery complex from above"></div>
    <div class="photo" style="left:410px;top:80px;width:115px;height:115px;background:linear-gradient(180deg,#a39a90,#7e6d5c 55%,#3b342d)" role="img" aria-label="Refinery towers at dusk"></div>
    <div class="caption" style="left:29px;top:233px"><b>DESIGN SOLUTION 01</b><div class="tiny">Enthusiastically matrix corporate capital performance channels.</div></div>
    <div class="caption" style="left:156px;top:233px"><b>DESIGN SOLUTION 02</b><div class="tiny">Enthusiastically matrix corporate capital performance channels.</div></div>
    <div class="caption" style="left:283px;top:233px"><b>DESIGN SOLUTION 03</b><div class="tiny">Enthusiastically matrix corporate capital performance channels.</div></div>
    <div class="caption" style="left:410px;top:233px"><b>DESIGN SOLUTION 04</b><div class="tiny">Enthusiastically matrix corporate capital performance channels.</div></div>
    <div class="foot-bar"></div><div class="foot-mark">IRONVALE</div><div class="foot-num">3</div>
  </section>

  <!-- 4: Stats with dark column -->
  <section class="slide" style="left:38px;top:1364px">
    <div class="hd-bar"></div><div class="hd-title">Text here</div>
    <div class="lead" style="left:58px;top:58px">Lorem ipsum dolor<br>sit amet, consectetuer<br>adipiscing elit.</div>
    <div class="foot-bar"></div><div class="foot-mark">IRONVALE</div><div class="foot-num">4</div>
    <div class="abs" style="left:272px;top:0;width:130px;height:312px;background:var(--ink)"></div>
    <div class="stat" style="left:58px;top:175px"><b>54+</b><i>LOREM</i><span>Professional corporate capital</span></div>
    <div class="stat" style="left:178px;top:175px"><b>50+</b><i>LOREM</i><span>Professional corporate capital</span></div>
    <div class="stat on-dark" style="left:298px;top:175px"><b>35+</b><i>LOREM</i><span>Professional corporate capital</span></div>
    <div class="stat" style="left:418px;top:175px"><b>25+</b><i>LOREM</i><span>Professional corporate capital</span></div>
  </section>

  <!-- 5: Stats with image strip -->
  <section class="slide" style="left:609px;top:1364px">
    <div class="hd-bar"></div><div class="hd-title">Text here</div>
    <div class="lead" style="left:58px;top:58px">Lorem ipsum dolor<br>sit amet, consectetuer<br>adipiscing elit.</div>
    <div class="stat" style="left:300px;top:68px"><b>50+</b><i>CLIENTS</i><span>Professional corporate capital</span></div>
    <div class="stat" style="left:420px;top:68px"><b>90+</b><i>PROJECTS</i><span>Professional corporate capital</span></div>
    <div class="photo" style="left:0;top:168px;width:92px;height:94px;background:linear-gradient(180deg,#b8b6ae,#8e8a7d 60%,#4d4a42)" role="img" aria-label="Pumpjacks in haze"></div>
    <div class="photo" style="left:92px;top:168px;width:92px;height:94px;background:linear-gradient(180deg,#c9b99d,#6f6352 60%,#2f2a24)" role="img" aria-label="Drilling rig against bright sky"></div>
    <div class="photo" style="left:184px;top:168px;width:92px;height:94px;background:linear-gradient(180deg,#9c8b7b,#5e5247 60%,#2e2823)" role="img" aria-label="Refinery towers at dusk"></div>
    <div class="photo" style="left:276px;top:168px;width:92px;height:94px;background:linear-gradient(180deg,#b1402e,#7d2a22 55%,#3a3a3a)" role="img" aria-label="Red refinery pipework"></div>
    <div class="photo" style="left:368px;top:168px;width:92px;height:94px;background:linear-gradient(180deg,#c7983f,#8a5d22 60%,#3a2a14)" role="img" aria-label="Pumpjack at golden sunset"></div>
    <div class="photo" style="left:460px;top:168px;width:91px;height:94px;background:linear-gradient(180deg,#8fb0d4,#8d8f94 50%,#5e6470)" role="img" aria-label="Refinery complex under blue sky"></div>
    <div class="foot-bar"></div><div class="foot-mark">IRONVALE</div><div class="foot-num">5</div>
  </section>

  <!-- 6: Team page -->
  <section class="slide" style="left:38px;top:1688px">
    <div class="hd-bar"></div><div class="hd-title">Team</div>
    <div class="team-box">
      <div class="member" style="left:6px;top:16px"><div class="portrait" role="img" aria-label="Portrait of Warren Ellsby"></div><h4>Warren Ellsby</h4><em>Managing Partner + CEO Redmesa Resources</em>Numerous oilfield operations leadership positions including VP &amp; GM for Frontera Drilling where he was responsible for 1000+ horizontal wells and 6000+ vertical wells</div>
      <div class="member" style="left:97px;top:16px"><div class="portrait" role="img" aria-label="Portrait of Neil Stanfield"></div><h4>Neil Stanfield</h4><i>Managing Partner, Ironvale</i><br>Extensive P&amp;L and management experience, including positions at Kaito Metals, a Global 50 electronic materials company.</div>
      <div class="member" style="left:188px;top:16px"><div class="portrait" role="img" aria-label="Portrait of Dale Whitcombe"></div><h4>Dale Whitcombe</h4><i>Operations Manager</i><br>Over 40 years of experience in oilfield operations, drilling, and equipment maintenance. Dale manages our daily field operations and production efforts.</div>
    </div>
    <div class="adv-title">ADVISORS</div>
    <div class="member" style="left:322px;top:70px;color:var(--ink)"><div class="portrait" role="img" aria-label="Portrait of Curtis Hale"></div><h4>Curtis Hale, P.E.</h4>Over 18 years experience in Permian Basin oil and gas operations including engineering, field, and executive leadership roles.</div>
    <div class="member" style="left:416px;top:70px;color:var(--ink)"><div class="portrait" role="img" aria-label="Portrait of Glen Marlow"></div><h4>Glen Marlow</h4><em><i>Reserves Analysis and Property Evaluation.</i></em>Registered Petroleum Engineer with 30+ years experience and significant background in the Permian Basin.</div>
    <div class="foot-bar"></div><div class="foot-mark">IRONVALE</div><div class="foot-num">6</div>
  </section>

  <!-- 7: Partners -->
  <section class="slide" style="left:609px;top:1688px">
    <div class="hd-bar"></div><div class="hd-title">Team</div>
    <div class="partner" style="left:88px;top:112px"><span class="sq"></span>Harlow Crest</div>
    <div class="partner" style="left:282px;top:104px"><span class="sq"></span>Pemberton, Vale &amp;<br>Ashcroft P.C.</div>
    <div class="partner" style="left:40px;top:170px"><span class="sq"></span>Prairie Federal Bank</div>
    <div class="partner" style="left:220px;top:170px"><span class="sq"></span>Stonemere Petroleum</div>
    <div class="partner" style="left:410px;top:170px"><span class="sq"></span>Kestrel Labs</div>
    <div class="foot-bar"></div><div class="foot-mark">IRONVALE</div><div class="foot-num">7</div>
  </section>

  <!-- 8: Stats with large images -->
  <section class="slide" style="left:38px;top:2012px">
    <div class="hd-bar"></div><div class="hd-title">Text here</div>
    <div class="lead" style="left:58px;top:58px">Lorem ipsum dolor<br>sit amet, consectetuer<br>adipiscing elit.</div>
    <div class="stat" style="left:310px;top:68px"><b>43+</b><i>DESIGNER</i><span>Professional corporate capital</span></div>
    <div class="stat" style="left:420px;top:68px"><b>50+</b><i>MARKETER</i><span>Professional corporate capital</span></div>
    <div class="photo" style="left:0;top:170px;width:184px;height:142px;background:linear-gradient(180deg,#c7983f,#8a5d22 60%,#3a2a14)" role="img" aria-label="Pumpjack at golden sunset"></div>
    <div class="photo" style="left:184px;top:170px;width:184px;height:142px;background:linear-gradient(180deg,#8fb0d4,#8d8f94 50%,#5e6470)" role="img" aria-label="Refinery complex from above"></div>
    <div class="photo" style="left:368px;top:170px;width:183px;height:142px;background:linear-gradient(180deg,#b1402e,#7d2a22 55%,#3a3a3a)" role="img" aria-label="Red refinery pipework"></div>
  </section>

  <!-- 9: Quote -->
  <section class="slide" style="left:609px;top:2012px">
    <div class="hd-bar"></div><div class="hd-title">Text here</div>
    <div class="abs" style="left:58px;top:80px;font-family:var(--sans);font-weight:300;font-size:16px;line-height:20px">Success is not a<br>good teacher, failure<br>makes you humble..</div>
    <p class="abs tiny" style="left:58px;top:178px;width:190px">Enthusiastically matrix corporate human capital vis-a-vis performance channels. Completely reinvent business process improvements for highly efficient markets. Rapidly administrate plug and play leadership without market positioning paradigms. Dramatically diverse intellectual capital through installed base competencies.</p>
    <div class="photo" style="left:278px;top:0;width:106px;height:154px;background:linear-gradient(180deg,#a39a90,#7e6d5c 55%,#3b342d)" role="img" aria-label="Refinery towers at dusk"></div>
    <div class="photo" style="left:278px;top:160px;width:106px;height:100px;background:linear-gradient(180deg,#8fb0d4,#8d8f94 50%,#5e6470)" role="img" aria-label="Refinery complex under blue sky"></div>
    <div class="photo" style="left:389px;top:99px;width:105px;height:103px;background:linear-gradient(180deg,#b1402e,#7d2a22 55%,#3a3a3a)" role="img" aria-label="Red refinery pipework"></div>
    <div class="foot-bar"></div><div class="foot-mark">IRONVALE</div><div class="foot-num">9</div>
  </section>

  <!-- 10: Table -->
  <section class="slide" style="left:38px;top:2336px">
    <div class="hd-bar"></div><div class="hd-title">Text here</div>
    <div class="tbl-head" style="left:34px">No</div>
    <div class="tbl-head" style="left:132px">PROJECT NAME</div>
    <div class="tbl-head" style="left:320px">AUTHOR</div>
    <div class="tbl-head" style="left:445px">PROCESS</div>
    <div class="tbl-row alt" style="top:74px"><span class="no">1</span><span class="pn">Seamlessly incentivize alternative best practices rather than</span><span class="au">Tom Reyes</span><span class="pr" style="width:100px"></span></div>
    <div class="tbl-row" style="top:97px"><span class="no">2</span><span class="pn">Proactively orchestrate competitive platforms</span><span class="au">Ana Brooks</span><span class="pr" style="width:85px"></span></div>
    <div class="tbl-row alt" style="top:120px"><span class="no">3</span><span class="pn">Authoritatively evolve standards compliant architectures</span><span class="au">Paul Carter</span><span class="pr" style="width:110px"></span></div>
    <div class="tbl-row" style="top:143px"><span class="no">4</span><span class="pn">Appropriately enhance unique intellectual</span><span class="au">Sam Doyle</span><span class="pr" style="width:42px"></span></div>
    <div class="tbl-row alt" style="top:166px"><span class="no">5</span><span class="pn">Conveniently create interoperable "outside the box"</span><span class="au">Ivy Nolan</span><span class="pr" style="width:95px"></span></div>
    <div class="tbl-row" style="top:189px"><span class="no">6</span><span class="pn">Holisticly streamline empowered experiences</span><span class="au">Rita Monroe</span><span class="pr" style="width:35px"></span></div>
    <div class="tbl-row alt" style="top:212px"><span class="no">7</span><span class="pn">Monotonectally harness cooperative functionalities after</span><span class="au">Lena Price</span><span class="pr" style="width:90px"></span></div>
    <div class="tbl-row" style="top:235px"><span class="no">8</span><span class="pn">Credibly simplify end-to-end</span><span class="au">Ruth Ellis</span><span class="pr" style="width:65px"></span></div>
    <div class="foot-bar"></div><div class="foot-mark">IRONVALE</div><div class="foot-num">10</div>
  </section>

  <!-- 11: Ring chart -->
  <section class="slide" style="left:609px;top:2336px">
    <div class="hd-bar"></div><div class="hd-title">Chart</div>
    <div class="ring" style="left:55px;top:85px">
      <svg width="90" height="90" viewBox="0 0 90 90"><circle cx="45" cy="45" r="38" fill="none" stroke="#0d0d0d" stroke-width="3" pathLength="100" stroke-dasharray="90 100" transform="rotate(-90 45 45)"/></svg>
      <div class="num">90<small>%</small></div><b>USAGE</b><div class="tiny">Enthusiastically corporate capital performance channels.</div>
    </div>
    <div class="ring" style="left:172px;top:85px">
      <svg width="90" height="90" viewBox="0 0 90 90"><circle cx="45" cy="45" r="38" fill="none" stroke="#0d0d0d" stroke-width="3" pathLength="100" stroke-dasharray="40 100" transform="rotate(-90 45 45)"/></svg>
      <div class="num">40<small>%</small></div><b>DESIGN</b><div class="tiny">Enthusiastically corporate capital performance channels.</div>
    </div>
    <div class="ring" style="left:290px;top:85px">
      <svg width="90" height="90" viewBox="0 0 90 90"><circle cx="45" cy="45" r="38" fill="none" stroke="#0d0d0d" stroke-width="3" pathLength="100" stroke-dasharray="75 100" transform="rotate(-90 45 45)"/></svg>
      <div class="num">75<small>%</small></div><b>CONTENT</b><div class="tiny">Enthusiastically corporate capital performance channels.</div>
    </div>
    <div class="ring" style="left:407px;top:85px">
      <svg width="90" height="90" viewBox="0 0 90 90"><circle cx="45" cy="45" r="38" fill="none" stroke="#0d0d0d" stroke-width="3" pathLength="100" stroke-dasharray="50 100" transform="rotate(-90 45 45)"/></svg>
      <div class="num">50<small>%</small></div><b>CREATIVITY</b><div class="tiny">Enthusiastically corporate capital performance channels.</div>
    </div>
    <div class="foot-bar"></div><div class="foot-mark">IRONVALE</div><div class="foot-num">11</div>
  </section>

  <!-- 12: Bar charts -->
  <section class="slide" style="left:38px;top:2660px">
    <div class="hd-bar"></div><div class="hd-title">Chart</div>
    <svg class="abs" style="left:0;top:0" width="551" height="312" viewBox="0 0 551 312" font-family="Roboto, Arial, sans-serif" font-size="4.5" fill="#8a8a8a">
      <g>
        <text x="58" y="107">125</text><text x="58" y="127">100</text><text x="62" y="146">75</text><text x="62" y="166">50</text><text x="62" y="185">25</text><text x="65" y="204">0</text>
        <rect x="88" y="170" width="5" height="33" fill="#c8c8c8"/><rect x="94" y="163" width="5" height="40" fill="#7a7a7a"/>
        <rect x="125" y="176" width="5" height="27" fill="#c8c8c8"/><rect x="131" y="168" width="5" height="35" fill="#7a7a7a"/>
        <rect x="162" y="166" width="5" height="37" fill="#c8c8c8"/><rect x="168" y="153" width="5" height="50" fill="#7a7a7a"/>
        <rect x="199" y="130" width="5" height="73" fill="#c8c8c8"/><rect x="205" y="160" width="5" height="43" fill="#7a7a7a"/>
        <rect x="236" y="175" width="5" height="28" fill="#c8c8c8"/><rect x="242" y="163" width="5" height="40" fill="#7a7a7a"/>
        <text x="83" y="212">Item 01</text><text x="120" y="212">Item 02</text><text x="157" y="212">Item 03</text><text x="194" y="212">Item 04</text><text x="231" y="212">Item 05</text>
      </g>
      <g>
        <text x="295" y="107">125</text><text x="295" y="127">100</text><text x="299" y="146">75</text><text x="299" y="166">50</text><text x="299" y="185">25</text><text x="302" y="204">0</text>
        <rect x="325" y="170" width="5" height="33" fill="#c8c8c8"/><rect x="331" y="163" width="5" height="40" fill="#7a7a7a"/>
        <rect x="362" y="176" width="5" height="27" fill="#c8c8c8"/><rect x="368" y="168" width="5" height="35" fill="#7a7a7a"/>
        <rect x="399" y="166" width="5" height="37" fill="#c8c8c8"/><rect x="405" y="153" width="5" height="50" fill="#7a7a7a"/>
        <rect x="436" y="130" width="5" height="73" fill="#c8c8c8"/><rect x="442" y="160" width="5" height="43" fill="#7a7a7a"/>
        <rect x="473" y="175" width="5" height="28" fill="#c8c8c8"/><rect x="479" y="163" width="5" height="40" fill="#7a7a7a"/>
        <text x="320" y="212">Item 01</text><text x="357" y="212">Item 02</text><text x="394" y="212">Item 03</text><text x="431" y="212">Item 04</text><text x="468" y="212">Item 05</text>
      </g>
    </svg>
    <div class="bar-caption" style="left:68px;top:234px"><b>MARKETING</b><div class="tiny">Enthusiastically matrix corporate capital performance. Completely reinvent process improvements for highly markets.</div></div>
    <div class="bar-caption" style="left:305px;top:234px"><b>DESIGN</b><div class="tiny">Enthusiastically matrix corporate capital performance. Completely reinvent process improvements for highly markets.</div></div>
    <div class="foot-bar"></div><div class="foot-mark">IRONVALE</div><div class="foot-num">12</div>
  </section>

  <!-- 13: Thank you -->
  <section class="slide" style="left:609px;top:2660px">
    <div class="photo" style="inset:0;background:linear-gradient(180deg,#c5c2b5 0%,#d8d5c9 40%,#a29d8c 70%,#5f5a4c 100%)" role="img" aria-label="Oil pumpjacks in a misty prairie field"></div>
    <div class="thanks">THANK YOU</div>
  </section>

</div>
</body>
</html>
```